Business Broker Graphics Package

Hi,

Seeking a smart and professional graphics package design including business card design (double-sided) and letterhead and PowerPoint slide template.

3 Deliverables:

1. Company Letterhead
2. Business Card (two sided) (will consider one sided designs)
3. PowerPoint Template. Requires cover PPT and 2nd page design.

For the prototype use this info:
Morgan Prelch QTR
Certified Business Intermediary
5817 Larkfield Rd.
Ellery, FL 34612
555.214.3096
Sample@Corvenlane.com
www.CorvenLane.com

I'll give exact information to winner to finalize later.

I've attached the logo..

Business card will be double sided and info for back of card is in attachment.

Look forward to your great ideas and concepts!
Updates

Project Deadline Extended
Reason: Just finalized logo design so now I'm ready to proceed with graphics package. Thanks!

Project Deadline Extended
Reason: More time to complete work! Thanks!

Target Market(s)

President's and business owners, CPA's and other professionals.

Industry/Entity Type

Business

Requirements
Nice to have
• Prefer horizontal card, but will consider vertical card design.

The business card should be all or primarily white. Text colors should be same as logo creative combination of black and forest green.

PowerPoint can be white background or lighter palette of colors I like gold color. I do not like darkly colored PowerPoint designs I prefer light and bright designs.

```html
<!DOCTYPE html>
<html lang="en">
<head>
<meta charset="utf-8">
<title>Corven Lane – Business Card</title>
<link rel="stylesheet" href="https://fonts.googleapis.com/css2?family=Josefin+Sans:wght@300;400;600&display=swap">
<style>
  :root {
    --backdrop: #ecebe8;
    --green-light: #4bb585;
    --green-mid: #3ca674;
    --green-deep: #2a8d5f;
    --green-edge: #1f7a50;
    --white: #ffffff;
    --ink: #1b1b1b;
  }
  * { box-sizing: border-box; margin: 0; padding: 0; }
  html, body { width: 1200px; height: 675px; overflow: hidden; }
  body {
    background: var(--backdrop);
    font-family: "Josefin Sans", "Helvetica Neue", Arial, sans-serif;
    position: relative;
  }
  .card {
    position: absolute;
    width: 400px;
    height: 224px;
    background: linear-gradient(135deg, var(--green-deep) 0%, var(--green-mid) 45%, var(--green-light) 70%, var(--green-mid) 100%);
    box-shadow:
      0 8px 0 -1px var(--green-edge),
      0 10px 0 -1px rgba(0,0,0,0.25),
      0 19px 0 -2px var(--green-mid),
      0 21px 4px -2px rgba(0,0,0,0.3);
    color: var(--white);
  }
  .card-front { left: 104px; top: 234px; }
  .card-back  { left: 686px; top: 233px; }

  .front-panel {
    position: absolute;
    left: 0; top: 0;
    width: 400px; height: 134px;
    background: var(--white);
    border-radius: 0 0 30px 30px;
    box-shadow: 0 4px 0 rgba(40,40,40,0.75), 0 6px 6px rgba(0,0,0,0.25);
    display: flex;
    align-items: center;
    justify-content: center;
    padding-top: 18px;
  }
  .brand-name {
    font-weight: 400;
    font-size: 22px;
    letter-spacing: 1px;
    color: var(--ink);
    line-height: 1;
    text-transform: uppercase;
  }
  .holder {
    position: absolute;
    left: 17px; top: 152px;
    font-style: normal;
    font-weight: 300;
    font-size: 9.6px;
    line-height: 12.4px;
  }
  .contact {
    position: absolute;
    left: 245px; top: 153px;
    list-style: none;
    font-weight: 300;
    font-size: 9.6px;
  }
  .contact li {
    display: flex; align-items: center;
    height: 16px;
  }
  .contact svg { width: 11px; height: 11px; margin-right: 8px; fill: var(--white); }

  .back-heading {
    position: absolute;
    left: 0; right: 0; top: 80px;
    text-align: center;
    font-weight: 300;
    font-size: 11px;
    letter-spacing: 0.3px;
  }
  .services {
    position: absolute;
    left: 0; right: 0; top: 100px;
    display: flex; justify-content: center;
    list-style: none;
    font-weight: 400;
    font-size: 11.4px;
  }
  .services li {
    padding: 2px 7px 1px;
    border-left: 1px solid var(--white);
    line-height: 16px;
  }
  .services li:first-child { border-left: none; }
</style>
</head>
<body>

<section class="card card-front" aria-label="Business card front">
  <div class="front-panel">
    <div class="brand-name">Corven Lane</div>
  </div>
  <address class="holder">
    Morgan Prelch QTR<br>
    Certified Business Intermediary<br>
    5817 Larkfield Rd.<br>
    Ellery, FL 34612
  </address>
  <ul class="contact">
    <li><svg viewBox="0 0 24 24" aria-hidden="true"><path d="M6.6 10.8a15.1 15.1 0 0 0 6.6 6.6l2.2-2.2a1 1 0 0 1 1-.25 11.4 11.4 0 0 0 3.6.57 1 1 0 0 1 1 1V20a1 1 0 0 1-1 1A17 17 0 0 1 3 4a1 1 0 0 1 1-1h3.5a1 1 0 0 1 1 1c0 1.25.2 2.45.57 3.57a1 1 0 0 1-.25 1z"/></svg>555.214.3096</li>
    <li><svg viewBox="0 0 24 24" aria-hidden="true"><path d="M2 5h20v2l-10 6L2 7z M2 9l10 6 10-6v10H2z"/></svg>Sample@Corvenlane.com</li>
    <li><svg viewBox="0 0 24 24" aria-hidden="true"><path d="M12 2a10 10 0 1 0 0 20 10 10 0 0 0 0-20zm0 2c.9 0 2.1 1.8 2.6 5H9.4C9.9 5.8 11.1 4 12 4zM4.3 11h3a18 18 0 0 0 .3 4H5a8 8 0 0 1-.7-4zm4.9 0h5.6a16 16 0 0 1-.3 4H9.5a16 16 0 0 1-.3-4zm7.5 0h3a8 8 0 0 1-.7 4h-2.6a18 18 0 0 0 .3-4z"/></svg>www.CorvenLane.com</li>
  </ul>
</section>

<section class="card card-back" aria-label="Business card back">
  <h2 class="back-heading">OWNERSHIP SOLUTIONS</h2>
  <ul class="services">
    <li>Sale / Acquisition</li>
    <li>Growth Engineer</li>
    <li>Exit Planning</li>
    <li>Valuation</li>
  </ul>
</section>

</body>
</html>
```